Young Makers Competition Event For Teenagers Needs Promo Graphics

I am in need of graphics for 2019 Northmere Young Makers Festival. It is a Young Makers competition event for teenagers. I need graphics to make an 11x17 poster and a main title graphic that I can use for digital (social, 16x9 for screens, etc). Graphic should include the following 2 logos: the QW Brightpath logo (this is who we are) and the "circles" logo is the logo of Young Makers Festival so that can be incorporated but is not mandatory and does not need to be in color. Tag line for Young Makers is "Discover. Develop. Deploy." Again, this is optional. Looking for an artistic design - geometric shapes, bright colors, or something along those lines. Something that speaks to teenagers and especially creatives/Young Makers types. Additionally, Post should include:
Maple Ridge Chapel
March 29-30
(registration & cost info may be added to the poster before design is finalized; still working on those details)

```html
<!DOCTYPE html>
<html lang="en">
<head>
<meta charset="utf-8">
<title>Northmere Young Makers Festival</title>
<link rel="stylesheet" href="https://fonts.googleapis.com/css2?family=Fira+Sans+Condensed:wght@500;600&family=Fira+Sans:wght@300&family=Kaushan+Script&display=swap">
<style>
  :root {
    --cyan: #5fe1f2;
    --slate: #4a5760;
    --yellow: #fbd000;
    --coral: #e07063;
    --white: #ffffff;
    --ink: #47535c;
    --sand: #f7d36a;
    --brand-blue: #2a9fd8;
  }
  * { margin: 0; padding: 0; box-sizing: border-box; }
  html, body { width: 848px; height: 1200px; overflow: hidden; background: var(--white); }
  .poster {
    position: relative;
    width: 848px;
    height: 1200px;
    overflow: hidden;
  }
  .backdrop {
    position: absolute;
    inset: 0;
    background:
      linear-gradient(160deg, var(--slate) 0%, var(--slate) 14%, var(--yellow) 24%, var(--cyan) 40%, var(--cyan) 55%, var(--slate) 68%, var(--coral) 82%, var(--cyan) 100%);
  }
  .stage {
    position: absolute;
    inset: 0;
  }
  .content {
    position: absolute;
    inset: 0;
    text-align: center;
  }
  .host-name {
    position: absolute;
    top: 252px;
    left: 0;
    width: 100%;
    font-family: "Fira Sans Condensed", sans-serif;
    font-weight: 600;
    font-size: 30px;
    color: var(--brand-blue);
  }
  .festival-mark {
    position: absolute;
    top: 370px;
    left: 0;
    width: 100%;
    display: flex;
    justify-content: center;
    align-items: center;
    gap: 12px;
    font-family: "Fira Sans Condensed", sans-serif;
    font-weight: 600;
    font-size: 24px;
    color: var(--ink);
  }
  .festival-mark .dot {
    width: 60px;
    height: 60px;
    border-radius: 50%;
    background: var(--brand-blue);
  }
  .region {
    position: absolute;
    top: 530px;
    left: 0;
    width: 100%;
    font-family: "Fira Sans Condensed", sans-serif;
    font-weight: 500;
    font-size: 33px;
    color: var(--sand);
  }
  .title {
    position: absolute;
    top: 580px;
    left: 0;
    width: 100%;
    font-family: "Kaushan Script", cursive;
    font-size: 68px;
    line-height: 1.1;
    color: var(--ink);
  }
  .tagline {
    position: absolute;
    top: 694px;
    left: 0;
    width: 100%;
    font-family: "Fira Sans Condensed", sans-serif;
    font-weight: 600;
    font-size: 34px;
    color: var(--yellow);
  }
  .date {
    position: absolute;
    top: 820px;
    left: 0;
    width: 100%;
    font-family: "Fira Sans Condensed", sans-serif;
    font-weight: 600;
    font-size: 58px;
    color: var(--coral);
  }
  .venue {
    position: absolute;
    top: 890px;
    left: 0;
    width: 100%;
    font-family: "Fira Sans", sans-serif;
    font-weight: 300;
    font-size: 32px;
    color: var(--ink);
  }
</style>
</head>
<body>
  <main class="poster">
    <div class="backdrop" role="img" aria-label="Bold painted brush strokes in cyan, slate, yellow and coral with scattered dots"></div>
    <svg class="stage" width="848" height="1200" viewBox="0 0 848 1200" aria-hidden="true">
      <path class="spotlight" fill="#ffffff"
        d="M420 160 C600 150 770 250 800 480 C825 690 790 900 650 1000 C540 1070 330 1060 210 1000 C80 930 40 760 45 560 C50 360 180 170 420 160 Z"/>
    </svg>
    <div class="content">
      <div class="host-name">QW Brightpath</div>
      <div class="festival-mark"><span class="dot"></span></div>
      <div class="region">Northmere</div>
      <h1 class="title">Young Makers Festival</h1>
      <p class="tagline">Discover. Develop. Deploy</p>
      <p class="date">29 - 30 MARCH</p>
      <p class="venue">Maple Ridge Chapel</p>
    </div>
  </main>
</body>
</html>
```